Progressive/contemporary business card design for successful Startups as a Service Company

New logo launched in 2020. New website launched in 2021. Now that COVID is (mostly) behind us, I'm networking with more people and need a business card that matches the company/logo design aesthetic.

```html
<!DOCTYPE html>
<html lang="en">
<head>
<meta charset="utf-8">
<title>BrightPath Business Card</title>
<link rel="stylesheet" href="https://fonts.googleapis.com/css2?family=Montserrat:wght@300;400;600&display=swap">
<style>
  :root {
    --bg: #1d1d1f;
    --card-white: #ffffff;
    --brand-blue: #0a6fc2;
    --text-grey: #4a4a4a;
    --accent-blue: #1a73c9;
    --accent-yellow: #f6b21a;
    --accent-red: #e8262b;
    --tone-orange: #f0722a;
    --tone-red: #e83a25;
    --tone-yellow: #f9b51c;
    --tone-blue: #1690d8;
    --tone-sky: #3dbdec;
    --tone-purple: #8e2a8e;
    --tone-magenta: #d9158a;
    --tone-green: #5fb748;
    --tone-lime: #a5cf3a;
  }
  * { box-sizing: border-box; margin: 0; padding: 0; }
  html, body { width: 1200px; height: 900px; overflow: hidden; }
  body {
    background: var(--bg);
    font-family: "Montserrat", sans-serif;
    display: flex;
    flex-direction: column;
    align-items: center;
    justify-content: center;
    gap: 56px;
  }
  .card {
    position: relative;
    width: 640px;
    height: 366px;
    border-radius: 26px;
    overflow: hidden;
    background: var(--card-white);
  }
  .poly-field {
    position: absolute;
    inset: 0;
    background:
      conic-gradient(from -10deg at 58% 52%,
        var(--tone-sky) 0deg, var(--tone-blue) 40deg,
        var(--tone-purple) 80deg, var(--tone-magenta) 160deg,
        var(--tone-green) 190deg, var(--tone-lime) 240deg,
        var(--tone-red) 255deg, var(--tone-orange) 290deg,
        var(--tone-yellow) 330deg, var(--tone-sky) 360deg);
  }
  .wordmark {
    position: absolute;
    color: #ffffff;
    font-weight: 400;
    letter-spacing: 0.22em;
    text-transform: uppercase;
    white-space: nowrap;
  }
  .card--front .wordmark {
    left: 50%;
    top: 50%;
    transform: translate(-50%, -50%);
    font-size: 42px;
  }
  .card--back .poly-field {
    background:
      conic-gradient(from -10deg at 68% 52%,
        var(--tone-sky) 0deg, var(--tone-blue) 40deg,
        var(--tone-purple) 80deg, var(--tone-magenta) 160deg,
        var(--tone-green) 190deg, var(--tone-lime) 240deg,
        var(--tone-red) 255deg, var(--tone-orange) 290deg,
        var(--tone-yellow) 330deg, var(--tone-sky) 360deg);
  }
  .contact-panel {
    position: absolute;
    inset: 0;
    background: var(--card-white);
    clip-path: polygon(0 0, 60% 0, 32% 100%, 0 100%);
    z-index: 1;
  }
  .accent-bar {
    position: absolute;
    left: 0;
    width: 5px;
    height: 34px;
    z-index: 2;
  }
  .accent-bar--blue { top: 30px; background: var(--accent-blue); }
  .accent-bar--yellow { top: 150px; background: var(--accent-yellow); }
  .accent-bar--red { top: 262px; background: var(--accent-red); }
  .contact {
    position: absolute;
    left: 34px;
    top: 34px;
    z-index: 2;
    color: var(--text-grey);
  }
  .contact__name {
    color: var(--brand-blue);
    font-weight: 600;
    font-size: 22px;
    letter-spacing: 0.02em;
  }
  .contact__role { font-size: 14px; margin-top: 2px; }
  .contact__address { font-size: 14px; line-height: 1.45; margin-top: 54px; }
  .contact__lines { list-style: none; margin-top: 44px; font-size: 14px; line-height: 1.5; }
  .contact__lines li { display: flex; align-items: center; gap: 8px; }
  .contact__lines svg { width: 12px; height: 12px; flex: none; }
  .card--back .wordmark {
    left: 318px;
    top: 196px;
    font-size: 26px;
    z-index: 2;
  }
</style>
</head>
<body>
  <section class="card card--front">
    <div class="poly-field" role="img" aria-label="Low-poly triangle pattern in orange, blue, purple and green"></div>
    <div class="wordmark">BrightPath</div>
  </section>

  <section class="card card--back">
    <div class="poly-field" role="img" aria-label="Low-poly triangle pattern in orange, blue, purple and green"></div>
    <div class="contact-panel"></div>
    <div class="wordmark">BrightPath</div>
    <span class="accent-bar accent-bar--blue"></span>
    <span class="accent-bar accent-bar--yellow"></span>
    <span class="accent-bar accent-bar--red"></span>
    <div class="contact">
      <h1 class="contact__name">DANIEL REYES</h1>
      <p class="contact__role">Director</p>
      <p class="contact__address">48 Harbor Lane<br>Maple Ridge, OR 97201</p>
      <ul class="contact__lines">
        <li>
          <svg viewBox="0 0 12 12"><path d="M3 1l2 2-1 1.5c.6 1.4 1.6 2.4 3 3L8.5 6.5l2 2L9 10.5C5 10 2 7 1.5 3z" fill="var(--brand-blue)"/></svg>
          555-014-2290
        </li>
        <li>
          <svg viewBox="0 0 12 12"><rect x="1" y="2.5" width="10" height="7" fill="none" stroke="var(--brand-blue)" stroke-width="1.2"/><path d="M1 2.5l5 4 5-4" fill="none" stroke="var(--brand-blue)" stroke-width="1.2"/></svg>
          hello@brightpathhq.com
        </li>
        <li>
          <svg viewBox="0 0 12 12"><circle cx="6" cy="6" r="5" fill="none" stroke="var(--brand-blue)" stroke-width="1.1"/><ellipse cx="6" cy="6" rx="2.2" ry="5" fill="none" stroke="var(--brand-blue)" stroke-width="1"/><path d="M1 6h10" stroke="var(--brand-blue)" stroke-width="1"/></svg>
          www.brightpathhq.com
        </li>
      </ul>
    </div>
  </section>
</body>
</html>
```